Brindle's Pot Labelling Project

We are a small fudge manufacturer based in Auckland, New Zealand and we're looking to revamp the look of our tubs in order to present a more professional looking product to the market and increase distribution. See our website @ www.kelvarsweets.co.nz to get a feel for our company and the fudge we make.

We have a number of flavours currently, and initial thoughts were to keep the labelling around the side of the tub uniform with the aim of keeping costs and inventory low, and allowing us to move into an In-Mould Label sooner as volumes grow. We're also looking for a top label which we envisaged as the method of identifying the flavour.
With the plan to move to IML in the future, and keeping costs low, the number of colours must also be taken into consideration.

The tubs we're planning to move to are the below dimensions:
Tub Height: 40 mm
Tub Circumference (bottom): 260 mm
Tub Circumference (top): 290 mm
Top Lid: 90 mm diameter

I've attached some images below:
- the tub
- our logo (we're happy to review the font used)
- our current label

Requirements
Must have
• - Room on the side for nutritional information & ingredient list (will differ by flavour)
- The words "Gluten Free" displayed.
- The words "Spoonable Fudge"
- The website address: www.kelvarsweets.co.nz
- Room for barcode (will differ by flavour)
Nice to have
• - Standard size stickers, so do not require customisation when printing.
- Easily applied stickers (taking into consideration the angled walls of the tub)
- Eye-catching
- Fun, but premium look and feel

```html
<!DOCTYPE html>
<html lang="en">
<head>
<meta charset="utf-8">
<title>Brindle's Pot – Spoonable Fudge Tub Labels</title>
<link rel="stylesheet" href="https://fonts.googleapis.com/css2?family=Nunito:wght@600;700;800&family=Arimo:wght@400;700&display=swap">
<style>
  :root {
    --mauve: #8b7470;
    --gold: #a98f4b;
    --gold-light: #c8b06c;
    --cocoa: #4e2f22;
    --cream: #ffffff;
    --ink: #1e1a18;
    --trim: #9a9a9a;
    --page: #ffffff;
  }
  html, body {
    margin: 0;
    padding: 0;
    width: 1200px;
    height: 714px;
    overflow: hidden;
    background: var(--page);
  }
  .label-sheet { display: block; width: 1200px; height: 714px; }
  .brand-name { font-family: "Nunito", sans-serif; font-weight: 800; fill: var(--cocoa); }
  .claim { font-family: "Nunito", sans-serif; font-weight: 700; fill: var(--cream); }
  .tagline { font-family: "Nunito", sans-serif; font-weight: 700; fill: var(--cream); }
  .side-url { font-family: "Nunito", sans-serif; font-weight: 700; fill: var(--cream); }
  .nf-title { font-family: "Arimo", sans-serif; font-weight: 700; fill: var(--ink); }
  .nf-note { font-family: "Arimo", sans-serif; fill: var(--ink); }
  .nf-cell { font-family: "Arimo", sans-serif; fill: var(--ink); }
  .nf-cell.bold { font-weight: 700; }
  .nf-rule { stroke: var(--ink); stroke-width: 0.6; }
  .nf-band { fill: var(--cocoa); }
  .nf-band-text { font-family: "Arimo", sans-serif; fill: var(--cream); }
  .nf-url { font-family: "Arimo", sans-serif; font-weight: 700; fill: var(--cocoa); }
  .trim-mark { stroke: var(--trim); stroke-width: 0.8; fill: none; }
  .gloss { fill: var(--cream); opacity: 0.35; }
</style>
</head>
<body>
<svg class="label-sheet" viewBox="0 0 1200 714" xmlns="http://www.w3.org/2000/svg">
  <defs>
    <linearGradient id="goldWave" x1="0" y1="0" x2="0" y2="1">
      <stop offset="0" stop-color="var(--gold-light)"/>
      <stop offset="0.35" stop-color="var(--gold)"/>
      <stop offset="1" stop-color="var(--gold)"/>
    </linearGradient>

    <clipPath id="curvedShape">
      <path d="M27,119.5 A1610 1610 0 0 1 1173,119.5 L1114.8,272.7 A1446 1446 0 0 0 85.2,272.7 Z"/>
    </clipPath>
    <clipPath id="flatShape">
      <path d="M25,487 Q60,505 120,505 L1020,505 Q1080,505 1113,487 L1113,686 L25,686 Z"/>
    </clipPath>

    <!-- arc guides for curved panel text -->
    <path id="bandLine1" d="M458.7,128.2 A1503 1503 0 0 1 741.3,128.2"/>
    <path id="bandLine2" d="M459.7,139.2 A1492 1492 0 0 1 740.3,139.2"/>
    <path id="bandLine3" d="M460.8,150.1 A1481 1481 0 0 1 739.2,150.1"/>
    <path id="urlLine" d="M462.4,168.5 A1462 1462 0 0 1 737.6,168.5"/>

    <!-- Nutrition heading and tables, 320 x 90 -->
    <symbol id="nutritionTop" viewBox="0 0 320 90">
      <text class="nf-title" x="12" y="18" font-size="12">Nutrition</text>
      <text class="nf-title" x="12" y="31" font-size="12">Facts</text>
      <text class="nf-note" x="12" y="45" font-size="8.5">Contains no artificial</text>
      <text class="nf-note" x="12" y="56" font-size="8.5">flavours, colours or</text>
      <text class="nf-note" x="12" y="67" font-size="8.5">additives.</text>

      <g class="nf-table" transform="translate(94,6)">
        <text class="nf-cell" x="0" y="6" font-size="6">Amount/Serving</text>
        <text class="nf-cell" x="100" y="6" font-size="6" text-anchor="end">Daily</text>
        <line class="nf-rule" x1="0" y1="9" x2="100" y2="9"/>
        <text class="nf-cell bold" x="0" y="18" font-size="6">Energy</text>
        <text class="nf-cell bold" x="100" y="18" font-size="6" text-anchor="end">0%</text>
        <line class="nf-rule" x1="0" y1="21" x2="100" y2="21"/>
        <text class="nf-cell" x="12" y="30" font-size="6">Protein</text>
        <text class="nf-cell" x="100" y="30" font-size="6" text-anchor="end">0%</text>
        <line class="nf-rule" x1="0" y1="33" x2="100" y2="33"/>
        <text class="nf-cell" x="22" y="42" font-size="6">Fat total 1g</text>
        <line class="nf-rule" x1="0" y1="45" x2="100" y2="45"/>
        <text class="nf-cell bold" x="0" y="54" font-size="6">Sodium 0mg</text>
        <text class="nf-cell bold" x="100" y="54" font-size="6" text-anchor="end">0%</text>
        <line class="nf-rule" x1="0" y1="57" x2="100" y2="57"/>
        <text class="nf-cell" x="12" y="66" font-size="6">Sugars</text>
        <text class="nf-cell" x="100" y="66" font-size="6" text-anchor="end">0%</text>
        <line class="nf-rule" x1="0" y1="69" x2="100" y2="69"/>
        <text class="nf-cell" x="0" y="78" font-size="6">Calcium</text>
        <text class="nf-cell bold" x="100" y="78" font-size="6" text-anchor="end">Vitamin 0%</text>
      </g>
      <g class="nf-table" transform="translate(206,6)">
        <text class="nf-cell" x="0" y="6" font-size="6">Amount/Serving</text>
        <text class="nf-cell" x="100" y="6" font-size="6" text-anchor="end">Daily</text>
        <line class="nf-rule" x1="0" y1="9" x2="100" y2="9"/>
        <text class="nf-cell bold" x="0" y="18" font-size="6">Energy</text>
        <text class="nf-cell bold" x="100" y="18" font-size="6" text-anchor="end">0%</text>
        <line class="nf-rule" x1="0" y1="21" x2="100" y2="21"/>
        <text class="nf-cell" x="12" y="30" font-size="6">Protein</text>
        <text class="nf-cell" x="100" y="30" font-size="6" text-anchor="end">0%</text>
        <line class="nf-rule" x1="0" y1="33" x2="100" y2="33"/>
        <text class="nf-cell" x="22" y="42" font-size="6">Fat total 1g</text>
        <line class="nf-rule" x1="0" y1="45" x2="100" y2="45"/>
        <text class="nf-cell bold" x="0" y="54" font-size="6">Sodium 0mg</text>
        <text class="nf-cell bold" x="100" y="54" font-size="6" text-anchor="end">0%</text>
        <line class="nf-rule" x1="0" y1="57" x2="100" y2="57"/>
        <text class="nf-cell" x="12" y="66" font-size="6">Sugars</text>
        <text class="nf-cell" x="100" y="66" font-size="6" text-anchor="end">0%</text>
        <line class="nf-rule" x1="0" y1="69" x2="100" y2="69"/>
        <text class="nf-cell" x="0" y="78" font-size="6">Calcium</text>
        <text class="nf-cell bold" x="100" y="78" font-size="6" text-anchor="end">Vitamin 0%</text>
      </g>
    </symbol>
  </defs>

  <!-- ===== Curved side label (tapered tub wall) ===== -->
  <g class="label label--curved">
    <g clip-path="url(#curvedShape)">
      <rect x="0" y="0" width="1200" height="300" fill="url(#goldWave)"/>
      <path class="mauve-field" d="M64.6,95 A1620 1620 0 0 1 436.3,12.3 L448.4,131.7 Q270,175 94.3,180 Z" fill="var(--mauve)"/>
      <path class="mauve-field" d="M763.7,12.3 A1620 1620 0 0 1 1135.4,95 L1105.7,180 Q930,175 751.6,131.7 Z" fill="var(--mauve)"/>
      <path class="info-panel" d="M436.3,5 L763.7,5 L746.1,185.4 L453.9,185.4 Z" fill="var(--cream)"/>
      <path class="nf-band" d="M447.2,119.8 A1512 1512 0 0 1 752.8,119.8 L749.2,155.6 A1476 1476 0 0 0 450.8,155.6 Z"/>
      <g transform="rotate(-9 600 1624)"><ellipse class="gloss" cx="600" cy="150" rx="9" ry="7"/></g>
      <g transform="rotate(16 600 1624)"><ellipse class="gloss" cx="600" cy="150" rx="9" ry="7"/></g>
    </g>

    <use href="#nutritionTop" x="455" y="22" width="290" height="82"/>
    <text class="nf-band-text" font-size="5.8"><textPath href="#bandLine1" startOffset="4"><tspan font-weight="700">Ingredients:</tspan> Sugar, cream, butter, milk solids, glucose, salt, natural vanilla.</textPath></text>
    <text class="nf-band-text" font-size="5.8"><textPath href="#bandLine2" startOffset="4"><tspan font-weight="700">Allergy Information:</tspan> Contains milk. Made in a facility that handles nuts.</textPath></text>
    <text class="nf-band-text" font-size="5.8"><textPath href="#bandLine3" startOffset="4"><tspan font-weight="700">Storage:</tspan> Keep cool and dry. Refrigerate after opening, best within days.</textPath></text>
    <text class="nf-url" font-size="8" text-anchor="middle"><textPath href="#urlLine" startOffset="50%">www.kelvarsweets.co.nz</textPath></text>

    <!-- left face -->
    <g class="brand-lockup" transform="rotate(-12.9 600 1624)">
      <circle cx="502" cy="69" r="11" fill="var(--cocoa)"/>
      <text class="brand-name" x="612" y="80" font-size="32" text-anchor="middle">Brindle's Pot</text>
    </g>
    <g transform="rotate(-8 600 1624)">
      <text class="claim" x="600" y="36" font-size="11" text-anchor="middle">Gluten Free</text>
    </g>
    <g transform="rotate(-12.6 600 1624)">
      <text class="tagline" x="600" y="163" font-size="28" text-anchor="middle">Spoonable Fudge</text>
    </g>
    <g transform="rotate(-20.1 600 1624)">
      <text class="side-url" x="600" y="96" font-size="11" text-anchor="middle" dominant-baseline="central" transform="rotate(-90 600 96)">www.kelvarsweets.co.nz</text>
    </g>

    <!-- right face -->
    <g class="brand-lockup" transform="rotate(12.4 600 1624)">
      <circle cx="502" cy="69" r="11" fill="var(--cocoa)"/>
      <text class="brand-name" x="612" y="80" font-size="32" text-anchor="middle">Brindle's Pot</text>
    </g>
    <g transform="rotate(17.5 600 1624)">
      <text class="claim" x="600" y="44" font-size="11" text-anchor="middle">Gluten Free</text>
    </g>
    <g transform="rotate(12.6 600 1624)">
      <text class="tagline" x="600" y="163" font-size="28" text-anchor="middle">Spoonable Fudge</text>
    </g>
    <g transform="rotate(20.1 600 1624)">
      <text class="side-url" x="600" y="96" font-size="11" text-anchor="middle" dominant-baseline="central" transform="rotate(90 600 96)">www.kelvarsweets.co.nz</text>
    </g>

    <line class="trim-mark" x1="8" y1="119.5" x2="20" y2="119.5"/>
    <line class="trim-mark" x1="1180" y1="119.5" x2="1192" y2="119.5"/>
    <line class="trim-mark" x1="90" y1="286" x2="96" y2="298"/>
    <line class="trim-mark" x1="1110" y1="286" x2="1104" y2="298"/>
  </g>

  <!-- ===== Flat side label ===== -->
  <g class="label label--flat">
    <g clip-path="url(#flatShape)">
      <rect x="25" y="480" width="1090" height="210" fill="var(--mauve)"/>
      <path d="M25,610 C110,600 200,625 300,595 C350,580 390,560 405,555 L405,686 L25,686 Z" fill="url(#goldWave)"/>
      <rect x="25" y="480" width="30" height="210" fill="var(--gold)"/>
      <path d="M730,555 C745,560 785,580 835,595 C935,625 1025,600 1113,610 L1113,686 L730,686 Z" fill="url(#goldWave)"/>
      <rect x="1083" y="480" width="32" height="210" fill="var(--gold)"/>
      <rect x="405" y="480" width="325" height="210" fill="var(--cream)"/>
      <ellipse class="gloss" cx="370" cy="655" rx="9" ry="7"/>
      <ellipse class="gloss" cx="1060" cy="655" rx="9" ry="7"/>
    </g>
    <use href="#nutritionTop" x="410" y="512" width="318" height="89"/>
    <rect class="nf-band" x="410" y="619" width="318" height="32"/>
    <text class="nf-band-text" x="420" y="628" font-size="5.8"><tspan font-weight="700">Ingredients:</tspan> Sugar, cream, butter, milk solids, glucose, salt, natural vanilla.</text>
    <text class="nf-band-text" x="420" y="637" font-size="5.8"><tspan font-weight="700">Allergy Information:</tspan> Contains milk. Made in a facility that handles nuts.</text>
    <text class="nf-band-text" x="420" y="646" font-size="5.8"><tspan font-weight="700">Storage:</tspan> Keep cool and dry. Refrigerate after opening, best within days.</text>
    <text class="nf-url" x="569" y="671" font-size="8" text-anchor="middle">www.kelvarsweets.co.nz</text>

    <g class="brand-lockup">
      <circle cx="132" cy="559" r="11" fill="var(--cocoa)"/>
      <text class="brand-name" x="150" y="570" font-size="32">Brindle's Pot</text>
    </g>
    <text class="claim" x="330" y="532" font-size="11">Gluten Free</text>
    <text class="tagline" x="232" y="645" font-size="27" text-anchor="middle">Spoonable Fudge</text>
    <text class="side-url" font-size="10" text-anchor="middle" transform="translate(43,585) rotate(-90)">www.kelvarsweets.co.nz</text>

    <g class="brand-lockup">
      <circle cx="822" cy="559" r="11" fill="var(--cocoa)"/>
      <text class="brand-name" x="840" y="570" font-size="32">Brindle's Pot</text>
    </g>
    <text class="claim" x="990" y="532" font-size="11">Gluten Free</text>
    <text class="tagline" x="910" y="645" font-size="27" text-anchor="middle">Spoonable Fudge</text>
    <text class="side-url" font-size="10" text-anchor="middle" transform="translate(1099,585) rotate(90)">www.kelvarsweets.co.nz</text>

    <line class="trim-mark" x1="570" y1="482" x2="570" y2="496"/>
    <line class="trim-mark" x1="10" y1="510" x2="22" y2="510"/>
    <line class="trim-mark" x1="1116" y1="510" x2="1128" y2="510"/>
    <line class="trim-mark" x1="25" y1="690" x2="25" y2="700"/>
    <line class="trim-mark" x1="1113" y1="690" x2="1113" y2="700"/>
  </g>
</svg>
</body>
</html>
```